buseisness card

design a card that similar to my web site
BRIXENTAPLORLLC .COM

Contact Information for Business Card

NAME PHONE # WEBSITE EMAIL AND DISCTIPTION OF WHAT WE DO

Colors
0054AA
0677BA
7BADD7
CADEEF
E8F1F8

Requirements
Must have
• lOGO AND DETAILS
Nice to have
• I LIKE THE WATER LIKE ON MY WEB SITE

```html
<!DOCTYPE html>
<html lang="en">
<head>
<meta charset="utf-8">
<title>Brixentaplor Business Card</title>
<link rel="stylesheet" href="https://fonts.googleapis.com/css2?family=Montserrat:wght@500;700&family=Roboto:wght@400;500;700&display=swap">
<style>
  :root {
    --bg: #e8e6e4;
    --brand-blue: #1a7aad;
    --deep-blue: #1f74b5;
    --card-white: #f3f4f5;
    --ink: #3a3a3a;
    --ink-strong: #2b2b2b;
    --pipe-light: #dde5ea;
    --pipe-mid: #cfd8de;
    --white: #ffffff;
  }
  * { margin: 0; padding: 0; box-sizing: border-box; }
  html, body { width: 1200px; height: 961px; overflow: hidden; background: var(--bg); }
  .canvas {
    width: 1200px; height: 961px; position: relative;
    display: flex; flex-direction: column; align-items: center; justify-content: center; gap: 60px;
  }
  .card {
    width: 580px; height: 332px; position: relative; overflow: hidden;
    box-shadow: 0 6px 18px rgba(0,0,0,0.12);
  }
  /* Front */
  .card-front {
    background: var(--brand-blue); color: var(--white);
    display: flex; flex-direction: column; align-items: center; justify-content: center;
  }
  .brand { display: flex; flex-direction: column; align-items: center; gap: 14px; }
  .brand-dot { width: 64px; height: 64px; border-radius: 50%; background: var(--white); }
  .brand-name {
    font-family: "Montserrat", sans-serif; font-weight: 700; font-size: 34px; letter-spacing: 1px;
  }
  .values {
    margin-top: 30px; font-family: "Montserrat", sans-serif; font-weight: 500; font-size: 11px;
    display: flex; flex-direction: column; align-items: center; gap: 6px;
  }
  .values-row { display: flex; gap: 16px; }
  .value { display: flex; align-items: center; gap: 5px; }
  .value svg { width: 12px; height: 12px; }
  /* Back */
  .card-back { background: var(--card-white); }
  .back-art {
    position: absolute; right: 0; top: 0; width: 300px; height: 260px;
    background: radial-gradient(ellipse at 55% 50%, var(--pipe-mid) 0%, var(--pipe-light) 45%, var(--card-white) 80%);
  }
  .edge-mark {
    position: absolute; left: 0; top: 196px; width: 20px; height: 28px; background: var(--deep-blue);
  }
  .back-details { position: absolute; left: 56px; top: 70px; }
  .back-brand { display: flex; align-items: center; gap: 10px; margin-bottom: 14px; }
  .back-brand .brand-dot { width: 30px; height: 30px; background: var(--deep-blue); }
  .back-brand .brand-name { font-size: 24px; color: var(--deep-blue); }
  .person-name {
    font-family: "Montserrat", sans-serif; font-weight: 700; font-size: 16px; color: var(--deep-blue);
  }
  .person-title {
    font-family: "Roboto", sans-serif; font-weight: 700; font-size: 13px; color: var(--ink-strong); margin-bottom: 8px;
  }
  .address, .contact-item {
    font-family: "Roboto", sans-serif; font-size: 14px; color: var(--ink); line-height: 1.35;
  }
  .contact-list { list-style: none; margin-top: 4px; }
  .contact-item { display: flex; align-items: center; gap: 8px; }
  .contact-item svg { width: 13px; height: 13px; flex: none; }
</style>
</head>
<body>
<main class="canvas">
  <section class="card card-front">
    <div class="brand">
      <span class="brand-dot"></span>
      <span class="brand-name">BRIXENTAPLOR</span>
    </div>
    <div class="values">
      <div class="values-row">
        <span class="value"><svg viewBox="0 0 12 12"><circle cx="6" cy="6" r="5" fill="none" stroke="#fff"/></svg>Cost Eefficient</span>
        <span class="value"><svg viewBox="0 0 12 12"><path d="M6 1 L11 10 H1 Z" fill="none" stroke="#fff"/></svg>Enviornmentally Friendly</span>
      </div>
      <div class="values-row">
        <span class="value"><svg viewBox="0 0 12 12"><rect x="4" y="1" width="4" height="10" rx="2" fill="none" stroke="#fff"/></svg>Thorough Testing</span>
        <span class="value"><svg viewBox="0 0 12 12"><rect x="1" y="2" width="10" height="8" fill="none" stroke="#fff"/></svg>Variation Testing</span>
        <span class="value"><svg viewBox="0 0 12 12"><rect x="2" y="1" width="8" height="10" fill="none" stroke="#fff"/></svg>Requirement Driven</span>
      </div>
    </div>
  </section>

  <section class="card card-back">
    <div class="back-art" role="img" aria-label="Illustration of leaking grey pipes with blue water drops and a red valve"></div>
    <span class="edge-mark"></span>
    <div class="back-details">
      <div class="back-brand">
        <span class="brand-dot"></span>
        <span class="brand-name">BRIXENTAPLOR</span>
      </div>
      <p class="person-name">MARCUS HOLLERBY</p>
      <p class="person-title">Managing Director</p>
      <p class="address">1840 Harbor Crest Drive<br>Dayton, OH 45402</p>
      <ul class="contact-list">
        <li class="contact-item"><svg viewBox="0 0 14 14"><path d="M3 1 L5.5 4 L4 6 Q6 9 8 10 L10 8.5 L13 11 L11 13 Q4 12 1 3 Z" fill="#1f74b5"/></svg>+740 555 0184</li>
        <li class="contact-item"><svg viewBox="0 0 14 14"><rect x="1" y="3" width="12" height="8" fill="none" stroke="#1f74b5" stroke-width="1.5"/><path d="M1 3 L7 8 L13 3" fill="none" stroke="#1f74b5" stroke-width="1.5"/></svg>mh@bx214.com</li>
        <li class="contact-item"><svg viewBox="0 0 14 14"><circle cx="7" cy="7" r="5.5" fill="none" stroke="#1f74b5" stroke-width="1.5"/><path d="M1.5 7 H12.5 M7 1.5 Q3.5 7 7 12.5 M7 1.5 Q10.5 7 7 12.5" fill="none" stroke="#1f74b5"/></svg>www.brixentaplorllc.com</li>
      </ul>
    </div>
  </section>
</main>
</body>
</html>
```